Business card design Needed for new logo / Construction business, home extensions and new builds

We need a business card design using our new logo files which i will attach to this project :)

We are a small construction business specialising in home extensions, new builds and property development. We are very ambitious and would appreciate professional and elegant designs for our new business card.

Very serious about using the services on BriefNest and recently acquired our new logo from here :)

Please get involved, i will feedback when i can as i am very busy but can respond daily, thanks

Target Market(s)

People that want to build onto their houses, new building developments or adding too their existing property

Industry/Entity Type

Construction

Contact Information for Business Card

Hollin Marsh Construction, Tobias Renwick (Managing Director), Tel 07822200444, email - info@hollin-marsh, www.hollin-marsh.co.uk

Colors

Designer to choose colors to be used in the design.

Requirements
Must have
• I like a deep grey on the back please. A lot of you have provided black from and back, try mixing things up a little. The black looks cool 😎 Thanks

```html
<!DOCTYPE html>
<html lang="en">
<head>
<meta charset="utf-8">
<title>Hollin Marsh Construction – Business Card</title>
<link rel="stylesheet" href="https://fonts.googleapis.com/css2?family=Cinzel:wght@400;500&display=swap">
<style>
  :root {
    --backdrop: #6f6f6f;
    --card-black: #050505;
    --deep-grey: #2e2e31;
    --card-white: #ffffff;
    --gold: #d9a124;
    --ink: #1a1a1a;
  }
  * { margin: 0; padding: 0; box-sizing: border-box; }
  html, body { width: 1200px; height: 850px; overflow: hidden; }
  body {
    background: var(--backdrop);
    font-family: "Cinzel", serif;
    position: relative;
  }
  .card {
    position: absolute;
    left: 324px;
    width: 552px;
    height: 330px;
    border-radius: 30px;
    overflow: hidden;
    box-shadow: 0 6px 18px rgba(0,0,0,0.35);
  }
  .card--front { top: 76px; background: var(--card-black); }
  .card--back { top: 443px; background: var(--card-white); }

  .pattern-fill { position: absolute; inset: 0; }
  .card--front .pattern-fill { background: radial-gradient(circle at 50% 45%, #141414 0%, #050505 70%); }
  .card--back .pattern-fill { background: linear-gradient(120deg, #ffffff 0%, #fdfaf2 100%); }

  .brand {
    position: absolute;
    left: 0; right: 0;
    top: 104px;
    text-align: center;
    color: var(--gold);
    font-weight: 500;
  }
  .brand__mark {
    width: 34px; height: 34px;
    margin: 0 auto 22px;
    background: var(--gold);
  }
  .brand__name {
    font-size: 27px;
    letter-spacing: 1.5px;
    line-height: 1.2;
  }

  .back-art { position: absolute; left: 0; top: 0; }

  .identity { position: absolute; left: 255px; top: 44px; white-space: nowrap; }
  .identity__name {
    font-size: 27px;
    font-weight: 500;
    color: var(--gold);
    letter-spacing: 1px;
    line-height: 1.15;
  }
  .identity__role {
    font-size: 15px;
    color: var(--ink);
    letter-spacing: 1px;
    margin-top: 2px;
  }

  .contacts { position: absolute; left: 255px; top: 0; list-style: none; }
  .contact {
    position: absolute;
    left: 0;
    display: flex;
    align-items: center;
    white-space: nowrap;
    font-size: 14px;
    color: var(--ink);
    letter-spacing: 0.8px;
  }
  .contact svg { width: 22px; height: 22px; margin-right: 15px; flex: none; }
  .contact--address { top: 139px; }
  .contact--email { top: 176px; }
  .contact--web { top: 208px; }
  .contact--phone { top: 245px; }
</style>
</head>
<body>

<svg width="0" height="0" style="position:absolute">
  <defs>
    <linearGradient id="gold-sheen" x1="0" y1="0" x2="1" y2="1">
      <stop offset="0" stop-color="#b8860f"/>
      <stop offset="0.45" stop-color="#f6d27a"/>
      <stop offset="0.7" stop-color="#d9a124"/>
      <stop offset="1" stop-color="#f3b62a"/>
    </linearGradient>
    <linearGradient id="silver-sheen" x1="0" y1="0" x2="1" y2="1">
      <stop offset="0" stop-color="#9a9a9c"/>
      <stop offset="0.5" stop-color="#e6e6e8"/>
      <stop offset="1" stop-color="#b5b5b7"/>
    </linearGradient>
  </defs>
</svg>

<section class="card card--front">
  <div class="pattern-fill" role="img" aria-label="Faint repeating brand pattern on black"></div>
  <div class="brand">
    <div class="brand__mark"></div>
    <p class="brand__name">Hollin Marsh<br>Construction</p>
  </div>
</section>

<section class="card card--back">
  <div class="pattern-fill" role="img" aria-label="Very faint repeating brand pattern on white"></div>

  <svg class="back-art" width="552" height="330" viewBox="0 0 552 330">
    <polygon points="0,0 106,0 209,166 106,330 0,330" fill="url(#silver-sheen)"/>
    <polygon points="0,0 97,0 199,166 97,330 0,330" fill="var(--deep-grey)"/>
    <polygon points="92,17 109,17 189,134 172,134" fill="url(#gold-sheen)"/>
    <polygon points="115,17 126,17 196,134 185,134" fill="url(#gold-sheen)"/>
    <polygon points="149,208 191,208 149,286 110,286" fill="url(#gold-sheen)"/>
  </svg>

  <div class="identity">
    <h1 class="identity__name">TOBIAS RENWICK</h1>
    <p class="identity__role">Managing Director</p>
  </div>

  <ul class="contacts">
    <li class="contact contact--address">
      <svg viewBox="0 0 22 22"><circle cx="11" cy="11" r="11" fill="url(#gold-sheen)"/><path d="M11 5a3.6 3.6 0 0 0-3.6 3.6C7.4 11.5 11 16 11 16s3.6-4.5 3.6-7.4A3.6 3.6 0 0 0 11 5z" fill="#fff"/><circle cx="11" cy="8.6" r="1.3" fill="var(--gold)"/></svg>
      Home extensions &amp; new builds
    </li>
    <li class="contact contact--email">
      <svg viewBox="0 0 22 22"><circle cx="11" cy="11" r="11" fill="url(#gold-sheen)"/><rect x="5.5" y="7.5" width="11" height="7.5" fill="#fff"/><path d="M5.5 7.5 11 12l5.5-4.5" fill="none" stroke="var(--gold)" stroke-width="0.9"/></svg>
      info@hollin-marsh
    </li>
    <li class="contact contact--web">
      <svg viewBox="0 0 22 22"><circle cx="11" cy="11" r="11" fill="url(#gold-sheen)"/><g fill="none" stroke="#fff" stroke-width="0.9"><circle cx="11" cy="11" r="5.5"/><ellipse cx="11" cy="11" rx="2.4" ry="5.5"/><path d="M5.5 11h11M6.3 8.2h9.4M6.3 13.8h9.4"/></g></svg>
      www.hollin-marsh.co.uk
    </li>
    <li class="contact contact--phone">
      <svg viewBox="0 0 22 22"><circle cx="11" cy="11" r="11" fill="url(#gold-sheen)"/><path d="M7.5 5.8c.5-.4 1.1-.3 1.4.2l1 1.7c.3.5.1 1-.3 1.3l-.7.5c.5 1.3 1.5 2.4 2.8 3l.5-.7c.3-.4.9-.6 1.3-.3l1.7 1c.5.3.6.9.2 1.4l-.8.9c-.6.6-1.6.7-2.4.3-2.4-1.2-4.3-3.1-5.4-5.5-.4-.8-.2-1.8.4-2.4z" fill="#fff"/></svg>
      Tel 07822200444
    </li>
  </ul>
</section>

</body>
</html>
```